Business Cards

The name of our firm is "Bayfield Insurance adjusters"
We separate ourselves from all other public adjusters because most of us worked for the insurance companies so we understand their games.
As Insurance adjusters we represent the Insured, not the insurance companies. Our # 1 priority is to handle the entire claim process as seamless as possible on behalf of the homeowner/business owner so they don't have to deal with the hassles and headaches. Just as the logo your team designed, I want the cards to stand out from everyone elses. I also want the cards to help better understand our services and Value on hiring us and value that we can offer.
I uploaded the logo whenever I created the project. I don't see an option on re uploading the logo anywhere. Any advise??

```html
<!DOCTYPE html>
<html lang="en">
<head>
<meta charset="utf-8">
<title>Bayfield Insurance Adjusters – Business Cards</title>
<link href="https://fonts.googleapis.com/css2?family=Montserrat:wght@500;600;700&display=swap" rel="stylesheet">
<style>
  :root {
    --backdrop: #444446;
    --card: #ffffff;
    --brand-blue: #0a5f8e;
    --brand-blue-deep: #065a8a;
    --ink-black: #1f1f20;
    --mist-grey: #d8d7d9;
    --mist-blue: #dfe5ef;
  }
  * { margin: 0; padding: 0; box-sizing: border-box; }
  html, body {
    width: 1200px; height: 1200px; overflow: hidden;
    background: var(--backdrop);
    font-family: "Montserrat", sans-serif;
  }
  .sheet {
    width: 1200px; height: 1200px;
    display: flex; flex-direction: column; align-items: center; justify-content: center;
    gap: 60px;
  }
  .card {
    position: relative;
    width: 820px; height: 470px;
    background: var(--card);
    border-radius: 28px;
    overflow: hidden;
    box-shadow: 0 6px 18px rgba(0,0,0,0.35);
  }
  .card-art { position: absolute; inset: 0; width: 100%; height: 100%; }
  .brand-name {
    color: var(--brand-blue);
    font-weight: 700;
    text-transform: uppercase;
    line-height: 1.1;
    letter-spacing: 0.02em;
  }
  .front .brand-name {
    position: absolute; left: 60px; top: 150px; width: 250px;
    font-size: 30px;
  }
  .contact {
    position: absolute; left: 360px; top: 140px;
    color: var(--brand-blue);
  }
  .contact-name { font-size: 44px; font-weight: 600; margin-bottom: 18px; }
  .contact-line { font-size: 23px; font-weight: 500; line-height: 1.35; }
  .back { display: flex; align-items: center; justify-content: center; }
  .back .brand-name { font-size: 40px; text-align: center; width: 360px; }
</style>
</head>
<body>
<main class="sheet">
  <section class="card front">
    <svg class="card-art" viewBox="0 0 820 470" aria-hidden="false">
      <defs>
        <linearGradient id="mistFade" x1="0" y1="0" x2="1" y2="0">
          <stop offset="0" stop-color="var(--mist-grey)"/>
          <stop offset="1" stop-color="var(--mist-blue)"/>
        </linearGradient>
      </defs>
      <rect x="330" y="0" width="490" height="400" fill="url(#mistFade)" opacity="0.75" role="img" aria-label="Faint large brand emblem decoration"/>
      <path class="accent-band" d="M400,372 C580,330 720,300 820,225 L820,272 C700,322 560,345 400,372 Z" fill="var(--ink-black)"/>
      <path class="wave-band" d="M110,470 C230,385 400,360 560,342 C680,328 760,305 820,268 L820,470 Z" fill="var(--brand-blue-deep)"/>
    </svg>
    <p class="brand-name">Bayfield Insurance Adjusters</p>
    <div class="contact">
      <p class="contact-name">Dario Velloso</p>
      <p class="contact-line">555-014-2287</p>
      <p class="contact-line">bayfieldclaims@example.com</p>
    </div>
  </section>
  <section class="card back">
    <p class="brand-name">Bayfield Insurance Adjusters</p>
  </section>
</main>
</body>
</html>
```